political campaign lawn sign - Governor's Council in Massachuesetts

We are looking for a political lawn sign. We are running a campaign for Governor's Council in Massachusetts. This sign will be on the lawn of homes and businesses so people driving by will see it. It needs to be simple and bold. The last name is long so maybe it could say vote for Marty and then Kolbeck will be big a bold on the next line??
We need it to say:
Vote for Martin Kolbeck
Governor's Council.

Target Market(s)

local residents

Industry/Entity Type

Politcal Campaign

Font styles to use
Sans Serif
Other font styles liked:
• not sure what font but a modern looking one such as Helvetica, Arial, Sans Seri, sharp sans..

Colors
0054AA
0677BA
7BADD7
CADEEF
E8F1F8
00AB8E
00BBA5
67D7C9
C6EFE9
E9F9F6
FFF300
FFF600
FEFA6F
FFFEC7
FFFEE8

Requirements
Must have
• My name written out with a Capital D and R but lower case for every other letter so its Marty Kolbeck
Nice to have
• modern font , the Colors of the lawn sign should have Blue, Yellow and White something bold that will stand out
Should not have
• any maps of Massachusetts

```html
<!DOCTYPE html>
<html lang="en">
<head>
<meta charset="utf-8">
<title>Vote for Martin Kolbeck – Governor's Council</title>
<link href="https://fonts.googleapis.com/css2?family=Arimo:wght@400;700&display=swap" rel="stylesheet">
<style>
  :root {
    --blue: #1358a8;
    --yellow: #f8f126;
    --slate: #7a8a94;
    --white: #ffffff;
    --edge: #1b1b1b;
  }
  * { margin: 0; padding: 0; box-sizing: border-box; }
  html, body { width: 1200px; height: 1200px; overflow: hidden; }
  body { background: var(--blue); font-family: "Arimo", Arial, Helvetica, sans-serif; }
  .sign { position: relative; width: 1200px; height: 1200px; background: var(--blue); border: 1px solid var(--edge); }
  .stripe { position: absolute; left: 0; width: 1200px; background: var(--yellow); border-top: 1px solid var(--edge); border-bottom: 1px solid var(--edge); }
  .stripe--thin { height: 20px; }
  .stripe--wide { height: 85px; left: 1px; width: 1199px; border-left: 1px solid var(--edge);
    background: linear-gradient(to right, var(--yellow) 0%, var(--yellow) 41%, var(--slate) 100%); }
  .headline, .office { position: absolute; left: 0; width: 1200px; text-align: center; color: var(--white); font-weight: 400; white-space: nowrap; }
  .headline { top: 338px; font-size: 162px; letter-spacing: -2px; line-height: 1; }
  .name-row { position: absolute; top: 560px; left: 0; width: 1200px; display: flex; justify-content: center; align-items: center; gap: 42px; }
  .surname { color: var(--yellow); font-weight: 700; font-size: 152px; letter-spacing: -3px; line-height: 1; }
  .arrow { width: 66px; height: 62px; flex: none; }
  .office { top: 752px; font-size: 118px; letter-spacing: -1px; line-height: 1; }
</style>
</head>
<body>
<div class="sign">
  <div class="stripe stripe--thin" style="top:37px"></div>
  <div class="stripe stripe--wide" style="top:75px"></div>
  <div class="stripe stripe--thin" style="top:178px"></div>

  <p class="headline">Vote for Martin</p>
  <div class="name-row">
    <svg class="arrow" viewBox="0 0 66 62" aria-hidden="true"><polygon points="0,20 34,20 34,0 66,31 34,62 34,42 0,42" fill="var(--yellow)"/></svg>
    <span class="surname">Kolbeck</span>
    <svg class="arrow" viewBox="0 0 66 62" aria-hidden="true"><polygon points="66,20 32,20 32,0 0,31 32,62 32,42 66,42" fill="var(--yellow)"/></svg>
  </div>
  <p class="office">Governer's Council</p>

  <div class="stripe stripe--thin" style="top:990px"></div>
  <div class="stripe stripe--wide" style="top:1028px"></div>
  <div class="stripe stripe--thin" style="top:1131px"></div>
</div>
</body>
</html>
```